Business card

I have changed logo's and colors. I have uploaded the new logo and colors.

In my head I am thinking about the main logo and text beside logo to be on one side of the card. The other side of the card to have just my picture and contact information.

The "R" emblem and the "equal housing" emblem... cut he MLS from the "R". and remove the wording from the house emblem.

Info on Card:

Lyle Penwarden
Designated Broker, CDPE, CNE, GRI
Direct: 602.555.0147
Fax: 623.555.0182
Lyle@PenwardenandPartners.example
www.PenwardenandPartners.example
4915 West Quillmoor Lane Glendale, AZ 85391

Please see brief as I have uploaded a new logo and a few notes.

Reason: I changed the logo and colors. Please see brief

I am leaning towards maybe a black business card(or at least on the front where the logo is). I liked several designs that were submitted. Please re-submit.

```html
<!DOCTYPE html>
<html lang="en">
<head>
<meta charset="utf-8">
<title>Penwarden &amp; Partners — Business Card</title>
<link rel="stylesheet" href="https://fonts.googleapis.com/css2?family=Cinzel:wght@400;600&family=Lato:wght@400;700;900&family=Nunito:ital,wght@1,800&display=swap">
<style>
  :root {
    --page-bg: #2b2b2b;
    --card-white: #ffffff;
    --card-shade: #eceeef;
    --teal: #6fa3aa;
    --teal-dark: #4f8790;
    --orange: #e8892a;
    --ink: #1d1d1d;
    --tagline-grey: #4a4a4a;
    --name-light: #e7eff0;
    --photo-top: #c9c3bc;
    --photo-bottom: #3a3d44;
  }
  * { box-sizing: border-box; margin: 0; padding: 0; }
  html, body { width: 1200px; height: 997px; overflow: hidden; }
  body {
    background: var(--page-bg);
    font-family: "Lato", sans-serif;
    position: relative;
  }
  .card {
    position: absolute;
    left: 250px;
    width: 700px;
    height: 400px;
    border-radius: 22px;
    overflow: hidden;
    background: linear-gradient(180deg, var(--card-white) 0%, var(--card-shade) 100%);
    box-shadow: 0 18px 40px rgba(0,0,0,.45);
  }
  .card--back { top: 60px; }
  .card--front { top: 527px; }

  /* Back */
  .back-band {
    position: absolute; left: 0; top: 0; width: 100%; height: 62px;
    background: var(--teal);
    border-bottom: 5px solid var(--orange);
  }
  .tagline {
    position: absolute; left: 60px; top: 150px;
    font-family: "Nunito", sans-serif; font-style: italic; font-weight: 800;
    font-size: 26px; color: var(--tagline-grey);
  }
  .tagline span { display: block; line-height: 1.55; }
  .tagline span:nth-child(2) { padding-left: 130px; }
  .tagline span:nth-child(3) { padding-left: 260px; }

  .brand {
    position: absolute; display: flex; align-items: center; gap: 10px;
  }
  .card--back .brand { right: 40px; top: 95px; }
  .card--front .brand { right: 40px; top: 26px; }
  .brand-dot {
    width: 52px; height: 52px; border-radius: 50%; background: var(--orange);
  }
  .brand-name {
    font-family: "Cinzel", serif; font-weight: 600; font-size: 22px;
    color: var(--teal-dark); line-height: 1.1;
  }

  /* Front */
  .photo {
    position: absolute; left: 40px; top: 92px; width: 230px; height: 230px;
    background: linear-gradient(180deg, var(--photo-top) 0%, var(--photo-bottom) 55%);
  }
  .contact {
    position: absolute; left: 300px; top: 118px;
    font-size: 15px; color: var(--ink);
  }
  .contact-row { display: flex; align-items: center; gap: 8px; margin-bottom: 9px; }
  .contact-row--split { gap: 22px; }
  .contact-web { font-weight: 900; }
  .contact-web .accent { color: var(--orange); }
  .contact-address { font-weight: 900; }
  .icon { width: 20px; height: 20px; flex: none; }
  .pair { display: flex; align-items: center; gap: 8px; }

  .front-band {
    position: absolute; left: 0; bottom: 0; width: 100%; height: 100px;
    background: var(--teal);
    border-top: 5px solid var(--orange);
  }
  .badges { position: absolute; right: 40px; top: 255px; display: flex; gap: 12px; align-items: flex-end; }
  .badge-house { width: 38px; height: 34px; background: var(--ink); }
  .badge-listing { width: 90px; height: 30px; background: var(--ink); }

  .agent {
    position: absolute; left: 40px; bottom: 18px; z-index: 2;
  }
  .agent-name {
    font-family: "Cinzel", serif; font-weight: 400; font-size: 30px;
    color: var(--name-light); letter-spacing: 1px;
  }
  .agent-title {
    font-weight: 900; font-size: 20px; color: var(--ink); text-transform: uppercase;
  }
</style>
</head>
<body>

  <section class="card card--back" aria-label="Card back">
    <div class="back-band"></div>
    <p class="tagline">
      <span>..One home at a time,</span>
      <span>..One friend at a time,</span>
      <span>..One client at a time,</span>
    </p>
    <div class="brand">
      <span class="brand-dot"></span>
      <span class="brand-name">Penwarden<br>&amp; Partners</span>
    </div>
  </section>

  <section class="card card--front" aria-label="Card front">
    <div class="brand">
      <span class="brand-dot"></span>
      <span class="brand-name">Penwarden<br>&amp; Partners</span>
    </div>

    <div class="front-band"></div>
    <div class="photo" role="img" aria-label="Portrait photo of the broker in a dark suit"></div>

    <div class="contact">
      <p class="contact-row contact-row--split">
        <span class="contact-web">www.<span class="accent">PenwardenandPartners</span>.example</span>
      </p>
      <p class="contact-row contact-row--split">
        <span class="pair">
          <svg class="icon" viewBox="0 0 20 20"><circle cx="10" cy="10" r="10" fill="#e8892a"/><path d="M6 5c1-1 2 0 2.5 1.5L7.7 8c.6 1.6 2 3 3.6 3.6l1.4-.8c1.5.5 2.5 1.5 1.5 2.5-1 1.2-3 1-5-.8S4.8 6.2 6 5z" fill="#fff"/></svg>
          602.555.0147
        </span>
        <span class="pair">
          <svg class="icon" viewBox="0 0 20 20"><circle cx="10" cy="10" r="10" fill="#e8892a"/><rect x="5" y="8" width="10" height="6" rx="1" fill="#fff"/><rect x="7" y="5" width="6" height="3" fill="#fff"/></svg>
          623.555.0182
        </span>
      </p>
      <p class="contact-row">
        <svg class="icon" viewBox="0 0 20 20"><circle cx="10" cy="10" r="10" fill="#e8892a"/><rect x="5" y="6.5" width="10" height="7" fill="#fff"/><path d="M5 6.5l5 4 5-4" stroke="#e8892a" fill="none"/></svg>
        Lyle@PenwardenandPartners.example
      </p>
      <p class="contact-row contact-address">4915 West Quillmoor Lane Glendale, AZ 85391</p>
    </div>

    <div class="badges">
      <span class="badge-house"></span>
      <span class="badge-listing"></span>
    </div>

    <div class="agent">
      <p class="agent-name">LYLE PENWARDEN</p>
      <p class="agent-title">Designated Broker, CDPE, CNE, GRI</p>
    </div>
  </section>

</body>
</html>
```